International Company needs a Letterhead & Envelope Design

Our Company name is Corvale Brightwick Limited.
We'd like to ask the Designers for the luxurious and sophisticated design. Our logo is very simple and neat with letter logos, so we look forward to more professional and refined designs from Designers.
We look forward to providing you with a great design.
Thanks very much in advance.

```html
<!DOCTYPE html>
<html lang="en">
<head>
<meta charset="utf-8">
<title>Corvale Brightwick Limited — Stationery</title>
<link rel="stylesheet" href="https://fonts.googleapis.com/css2?family=Lato:wght@400;700&display=swap">
<style>
  :root {
    --backdrop: #707070;
    --paper: #efefef;
    --paper-flap: #f3f3f3;
    --ink: #5b5b5b;
    --rule: #9a9a9a;
    --edge: #d4d4d4;
    --shadow: rgba(0, 0, 0, 0.28);
    --shadow-soft: rgba(0, 0, 0, 0.16);
  }
  html, body {
    margin: 0;
    width: 1200px;
    height: 947px;
    overflow: hidden;
    background: var(--backdrop);
    font-family: "Lato", Arial, sans-serif;
    color: var(--ink);
  }
  .stage { position: relative; width: 1200px; height: 947px; }

  .letterhead {
    position: absolute; left: 61px; top: 82px;
    width: 553px; height: 780px;
    background: var(--paper);
    box-shadow: 0 1px 3px var(--shadow-soft);
  }
  .wordmark {
    font-family: "Lato", Arial, sans-serif;
    font-weight: 700;
    color: var(--ink);
    letter-spacing: 0.04em;
    line-height: 1;
    white-space: nowrap;
  }
  .letterhead .wordmark { position: absolute; left: 40px; top: 79px; font-size: 21px; }

  .contact-block {
    position: absolute; left: 413px; top: 52px;
    border-left: 1px solid var(--rule);
    padding: 2px 0 4px 10px;
    font-size: 7.4px; line-height: 9.5px;
  }
  .contact-block .address { margin: 0 0 6px; }
  .contact-list { list-style: none; margin: 0; padding: 0; }
  .contact-list li { display: flex; align-items: center; height: 11px; }
  .contact-list svg { width: 7px; height: 7px; margin-right: 6px; fill: var(--ink); }

  .envelope-back {
    position: absolute; left: 570px; top: 382px;
    width: 579px; height: 288px;
    background: var(--paper);
    box-shadow: -2px 1px 5px var(--shadow);
  }
  .envelope-back .flap {
    position: absolute; left: 0; top: 0; width: 579px; height: 84px;
    filter: drop-shadow(0 2px 2px var(--shadow-soft));
  }
  .envelope-back .wordmark {
    position: absolute; left: 0; width: 579px; top: 34px;
    text-align: center; font-size: 19px;
  }

  .envelope-front {
    position: absolute; left: 475px; top: 531px;
    width: 634px; height: 290px;
    background: var(--paper);
    border-top: 1px solid var(--edge);
    border-left: 1px solid var(--edge);
    box-shadow: -3px 1px 6px var(--shadow);
  }
  .return-address {
    position: absolute; left: 35px; top: 40px;
    text-align: center;
  }
  .return-address .wordmark { font-size: 19px; display: block; margin-bottom: 6px; }
  .return-address p { margin: 0; font-size: 7.4px; line-height: 9.5px; }
</style>
</head>
<body>
<main class="stage">

  <section class="letterhead" aria-label="Letterhead">
    <div class="wordmark">CORVALE</div>
    <div class="contact-block">
      <p class="address">4127 Harrowgate Lane<br>Linden Hollow, NY 11460</p>
      <ul class="contact-list">
        <li><svg viewBox="0 0 10 10"><path d="M1 4 C2 1 8 1 9 4 L7 5 L6 3.5 H4 L3 5 Z M2 6 H8 V9 H2 Z"/></svg>555 0142 7731</li>
        <li><svg viewBox="0 0 10 10"><path d="M3 0 H7 A1 1 0 0 1 8 1 V9 A1 1 0 0 1 7 10 H3 A1 1 0 0 1 2 9 V1 A1 1 0 0 1 3 0 Z M3 1.5 V8 H7 V1.5 Z"/></svg>555 0198 2460</li>
        <li><svg viewBox="0 0 10 10"><path d="M3 0 H7 V3 H3 Z M0 3.5 H10 V8 H8 V10 H2 V8 H0 Z M3 6.5 V8.8 H7 V6.5 Z"/></svg>555 0177 3814</li>
        <li><svg viewBox="0 0 10 10"><path d="M0 2 H10 V8 H0 Z M0.5 2.5 L5 5.5 L9.5 2.5 Z"/></svg>elena@corvale.com</li>
        <li><svg viewBox="0 0 10 10"><circle cx="5" cy="5" r="5"/></svg>www.corvale.com</li>
      </ul>
    </div>
  </section>

  <section class="envelope-back" aria-label="Envelope reverse">
    <svg class="flap" viewBox="0 0 579 84" aria-hidden="true">
      <path d="M0 0 H579 L562 60 Q556 80 536 81 H42 Q22 80 16 60 Z" fill="var(--paper-flap)" stroke="var(--edge)" stroke-width="1"/>
    </svg>
    <div class="wordmark">CORVALE</div>
  </section>

  <section class="envelope-front" aria-label="Envelope front">
    <div class="return-address">
      <span class="wordmark">CORVALE</span>
      <p>4127 Harrowgate Lane<br>Linden Hollow, NY 11460</p>
    </div>
  </section>

</main>
</body>
</html>
```